Copper Lantern Advisory: Ebook Project Cover Design Needed

I recently finished writing Copper Lantern Advisory and I need the front cover and back cover for the ebook.

I'm looking for people to want to open it based on the cover online, as I won't sell it in traditional bookstores. I'd like the ebook cover, as well as for the physical book in the 6x9 format.

```html
<!DOCTYPE html>
<html lang="en">
<head>
<meta charset="utf-8">
<title>Copper Lantern Advisory — Book Cover</title>
<link rel="stylesheet" href="https://fonts.googleapis.com/css2?family=Bebas+Neue&family=Montserrat:wght@500;600&display=swap">
<style>
  :root {
    --backdrop: #a6a7aa;
    --cover-black: #000000;
    --ink: #111111;
    --author-white: #ffffff;
    --gold-light: #f2f0b0;
    --gold-mid: #ecd274;
    --gold-warm: #e3c27e;
    --gold-deep: #c08d48;
    --silver-light: #eff3f5;
    --silver-mid: #c8d1d3;
    --silver-top: #d8dcdf;
    --silver-deep: #aeaeb0;
  }
  html, body {
    margin: 0;
    padding: 0;
    width: 1200px;
    height: 1200px;
    overflow: hidden;
    background: var(--backdrop);
  }
  .canvas {
    position: relative;
    width: 1200px;
    height: 1200px;
    background: radial-gradient(ellipse at 50% 50%, #98999c 0%, var(--backdrop) 60%);
  }
  .book-cover {
    position: absolute;
    left: 273px;
    top: 110px;
    width: 653px;
    height: 979px;
    background: var(--cover-black);
    box-shadow: 0 20px 60px rgba(0, 0, 0, 0.28);
  }
  .book-cover svg {
    display: block;
    width: 653px;
    height: 979px;
  }
  .title-line {
    font-family: "Bebas Neue", "Oswald", sans-serif;
  }
  .tagline {
    font-family: "Montserrat", sans-serif;
    font-weight: 600;
    font-size: 20px;
    fill: var(--ink);
  }
  .author-name {
    font-family: "Montserrat", sans-serif;
    font-weight: 600;
    font-size: 50px;
    fill: var(--author-white);
  }
</style>
</head>
<body>
<div class="canvas">
  <div class="book-cover">
    <svg viewBox="0 0 653 979" xmlns="http://www.w3.org/2000/svg">
      <defs>
        <linearGradient id="gold-large" x1="0" y1="0" x2="0" y2="1">
          <stop offset="0" stop-color="var(--gold-warm)"/>
          <stop offset="0.3" stop-color="var(--gold-light)"/>
          <stop offset="0.7" stop-color="var(--gold-mid)"/>
          <stop offset="1" stop-color="var(--gold-deep)"/>
        </linearGradient>
        <linearGradient id="silver-metal" x1="0" y1="0" x2="0" y2="1">
          <stop offset="0" stop-color="var(--silver-top)"/>
          <stop offset="0.38" stop-color="var(--silver-mid)"/>
          <stop offset="0.75" stop-color="var(--silver-light)"/>
          <stop offset="1" stop-color="var(--silver-deep)"/>
        </linearGradient>
        <linearGradient id="gold-small" x1="0" y1="0" x2="0" y2="1">
          <stop offset="0" stop-color="var(--gold-warm)"/>
          <stop offset="0.45" stop-color="var(--gold-light)"/>
          <stop offset="1" stop-color="var(--gold-mid)"/>
        </linearGradient>
        <linearGradient id="gold-band" x1="0" y1="0" x2="1" y2="0">
          <stop offset="0" stop-color="#e2bf75"/>
          <stop offset="0.6" stop-color="var(--gold-light)"/>
          <stop offset="1" stop-color="#ede07f"/>
        </linearGradient>
      </defs>

      <g class="cover-title">
        <text class="title-line" x="59" y="332" font-size="347" fill="url(#gold-large)" stroke="#d9b266" stroke-width="1.5" textLength="536" lengthAdjust="spacingAndGlyphs">COPPER</text>
        <text class="title-line" x="59" y="519" font-size="229" fill="url(#silver-metal)" stroke="#e6e9eb" stroke-width="1.5" textLength="536" lengthAdjust="spacingAndGlyphs">LANTERN</text>
        <text class="title-line" x="59" y="633" font-size="123" fill="url(#gold-small)" textLength="536" lengthAdjust="spacingAndGlyphs">ADVISORY</text>
      </g>

      <g class="tagline-band">
        <rect x="0" y="691" width="653" height="143" fill="url(#gold-band)"/>
        <line x1="0" y1="707" x2="653" y2="707" stroke="var(--ink)" stroke-width="1"/>
        <line x1="0" y1="817" x2="653" y2="817" stroke="var(--ink)" stroke-width="1"/>
        <text class="tagline" text-anchor="middle">
          <tspan x="326" y="745">Lorem ipsum dolor sit amet, consectetuer</tspan>
          <tspan x="326" y="769">adipiscing elit, sed diam nonummy nibh</tspan>
          <tspan x="326" y="793">euismod tincidunt ut laore.</tspan>
        </text>
      </g>

      <text class="author-name" x="326" y="940" text-anchor="middle" textLength="533" lengthAdjust="spacingAndGlyphs">AUTHOR NAME HERE</text>
    </svg>
  </div>
</div>
</body>
</html>
```